Business card logo

Hello, I would like a business card for my law firm with a logo composed of my initials "MH". The logo is intended to appear on my business card, my letterhead, envelope and documents from my office. My first and last name (Maren Holt) and "Lawyer" must appear next to the logo. I would like the logo and the characters to be in golden color on a dark background (example black, navy blue). I would especially like a refined work on the logo which should be composed of the letters J and R.

```html
<!DOCTYPE html>
<html lang="en">
<head>
<meta charset="utf-8">
<title>Maren Holt — Business Card</title>
<link href="https://fonts.googleapis.com/css2?family=Work+Sans:wght@400;500;600&display=swap" rel="stylesheet">
<style>
  :root {
    --stage: #1d1d1e;
    --navy: #0f3558;
    --navy-pattern: #133d63;
    --gold: #a8925f;
    --paper: #ffffff;
    --ink: #3a3a3c;
    --ink-soft: #5a5a5c;
  }
  * { margin: 0; padding: 0; box-sizing: border-box; }
  html, body { width: 1200px; height: 878px; overflow: hidden; }
  body {
    background: var(--stage);
    font-family: "Work Sans", sans-serif;
    position: relative;
  }
  .card {
    position: absolute;
    width: 620px;
    height: 354px;
    border-radius: 2px;
    box-shadow: 0 14px 30px rgba(0,0,0,.45);
    overflow: hidden;
  }
  /* Back face */
  .card-back {
    left: 90px; top: 56px;
    background: var(--navy);
  }
  .card-back .pattern {
    position: absolute; inset: 0;
    background: linear-gradient(135deg, var(--navy) 0%, var(--navy-pattern) 50%, var(--navy) 100%);
  }
  .card-back .mark {
    position: absolute;
    right: 64px; top: 96px;
    display: flex; align-items: center; gap: 8px;
    color: var(--gold);
    font-weight: 600;
    font-size: 15px;
    letter-spacing: 2px;
    text-transform: uppercase;
  }
  .mark-square {
    width: 8px; height: 8px; background: var(--gold);
  }
  /* Front face */
  .card-front {
    left: 490px; top: 466px;
    background: var(--paper);
  }
  .front-mark {
    position: absolute;
    right: 44px; top: 62px;
    display: flex; align-items: center; gap: 10px;
    color: var(--gold);
    font-weight: 600;
    font-size: 24px;
    letter-spacing: 3px;
    text-transform: uppercase;
  }
  .front-mark .mark-square { width: 10px; height: 10px; }
  .name-bar {
    position: absolute;
    left: 0; top: 150px;
    width: 10px; height: 38px;
    background: var(--gold);
  }
  .holder {
    position: absolute;
    left: 34px; top: 148px;
  }
  .holder-name {
    color: var(--gold);
    font-weight: 600;
    font-size: 25px;
    letter-spacing: 1px;
    text-transform: uppercase;
    line-height: 1;
  }
  .holder-role {
    color: var(--ink-soft);
    font-size: 15px;
    margin-top: 4px;
  }
  .rule {
    position: absolute;
    left: 34px; right: 40px; top: 222px;
    height: 1.5px; background: var(--gold);
  }
  .contacts {
    position: absolute;
    left: 34px; top: 250px;
    list-style: none;
    color: var(--ink);
    font-size: 17px;
    line-height: 27px;
  }
  .contacts li { display: flex; align-items: center; gap: 9px; }
  .contacts svg { width: 12px; height: 12px; flex: none; }
  .address {
    position: absolute;
    right: 40px; bottom: 30px;
    text-align: right;
    color: var(--ink);
    font-size: 17px;
    line-height: 25px;
    font-style: normal;
  }
</style>
</head>
<body>

<section class="card card-back" aria-label="Card back">
  <div class="pattern" role="img" aria-label="Faint repeated monogram pattern across the navy back"></div>
  <div class="mark"><span class="mark-square"></span>Maren Holt</div>
</section>

<section class="card card-front" aria-label="Card front">
  <div class="front-mark"><span class="mark-square"></span>Maren Holt</div>

  <div class="name-bar"></div>
  <div class="holder">
    <p class="holder-name">Maren Holt</p>
    <p class="holder-role">Lawyer</p>
  </div>
  <div class="rule"></div>

  <ul class="contacts">
    <li>
      <svg viewBox="0 0 12 12" aria-hidden="true"><path d="M3 1l2 2.5-1.2 1.2c.6 1.3 1.6 2.3 2.9 2.9L7.9 6.4 10.5 8.5 9.3 10.8C5.2 10.4 1.6 6.8 1.2 2.7z" fill="var(--gold)"/></svg>
      555-014-2290
    </li>
    <li>
      <svg viewBox="0 0 12 12" aria-hidden="true"><rect x="1" y="2.5" width="10" height="7" fill="none" stroke="var(--gold)" stroke-width="1.1"/><path d="M1 2.5l5 4 5-4" fill="none" stroke="var(--gold)" stroke-width="1.1"/></svg>
      info@MarenHolt.com
    </li>
    <li>
      <svg viewBox="0 0 12 12" aria-hidden="true"><circle cx="6" cy="6" r="5" fill="none" stroke="var(--gold)" stroke-width="1"/><ellipse cx="6" cy="6" rx="2.2" ry="5" fill="none" stroke="var(--gold)" stroke-width="1"/><path d="M1 6h10" stroke="var(--gold)" stroke-width="1"/></svg>
      www.MarenHolt.com
    </li>
  </ul>

  <address class="address">
    418 Larch Street<br>
    Brookfield, IN 47291
  </address>
</section>

</body>
</html>
```